Desk Allies Business Card

Contact Information for Business Card

Jaakko Virtanola
Managing Director

3/47 Darrow Lane Belmont ACT 2915

Tel: +61 02 6187 4326
Mob: +61 0432 715 649

Email: jaakko@deskallies-example.com.au
Web: www.deskallies-example.com.au

Colors

Designer to choose colors to be used in the design.

Requirements
Must have
• Logo, Name, Title, Address, Telephone, Mobile, Email Address and Website
• "Desk Ally Worldwide Pty Ltd"

```html
<!DOCTYPE html>
<html lang="en">
<head>
<meta charset="utf-8">
<title>Desk Allies Business Card</title>
<link rel="stylesheet" href="https://fonts.googleapis.com/css2?family=Montserrat:wght@400;600;700&family=Roboto:wght@400&display=swap">
<style>
  :root {
    --bg: #e4e4e2;
    --card: #fbfbfa;
    --blue: #2f7fc4;
    --ink: #262626;
    --grey: #6d6d6d;
    --shadow: rgba(0,0,0,0.14);
  }
  * { margin: 0; padding: 0; box-sizing: border-box; }
  html, body { width: 1200px; height: 1000px; overflow: hidden; }
  body { background: var(--bg); font-family: "Montserrat", sans-serif; position: relative; }

  .card {
    position: absolute;
    left: 305px;
    width: 590px;
    height: 330px;
    background: var(--card);
    box-shadow: 0 4px 10px var(--shadow);
  }
  .card--front { top: 140px; }
  .card--back { top: 530px; }

  /* Front */
  .brand {
    position: absolute;
    left: 105px;
    top: 134px;
    display: flex;
    align-items: center;
    gap: 14px;
  }
  .brand__dot { width: 56px; height: 56px; border-radius: 50%; background: var(--blue); }
  .brand__name {
    font-weight: 600;
    font-size: 30px;
    letter-spacing: 0.5px;
    color: var(--blue);
    text-transform: uppercase;
    line-height: 1;
  }
  .brand__tagline {
    margin-top: 5px;
    font-weight: 400;
    font-size: 10.5px;
    letter-spacing: 2.6px;
    color: var(--grey);
    text-transform: uppercase;
  }

  /* Back */
  .back-mark {
    position: absolute;
    left: 70px;
    top: 108px;
    width: 150px;
    display: flex;
    flex-direction: column;
    align-items: center;
    gap: 12px;
  }
  .back-mark__dot { width: 130px; height: 130px; border-radius: 50%; background: var(--blue); }
  .back-mark__name { font-weight: 600; font-size: 18px; color: var(--blue); text-transform: uppercase; }

  .identity { position: absolute; left: 270px; top: 52px; }
  .identity__company { font-weight: 700; font-size: 12px; color: var(--ink); }
  .identity__person {
    margin-top: 2px;
    font-weight: 700;
    font-size: 23px;
    letter-spacing: 0.6px;
    color: var(--blue);
    text-transform: uppercase;
  }
  .identity__role { font-weight: 400; font-size: 18px; color: #3a3a3a; letter-spacing: 0.4px; }

  .contacts {
    position: absolute;
    left: 285px;
    top: 150px;
    list-style: none;
    font-family: "Roboto", sans-serif;
    font-size: 13.5px;
    color: #3a3a3a;
  }
  .contacts li { display: flex; align-items: center; gap: 12px; height: 18px; }
  .contacts svg { width: 12px; height: 12px; fill: var(--blue); flex: none; }
</style>
</head>
<body>

<section class="card card--front">
  <div class="brand">
    <span class="brand__dot"></span>
    <div>
      <div class="brand__name">Desk Allies</div>
      <div class="brand__tagline">Ergonomic Office Environments</div>
    </div>
  </div>
</section>

<section class="card card--back">
  <div class="back-mark">
    <span class="back-mark__dot"></span>
    <span class="back-mark__name">Desk Allies</span>
  </div>

  <div class="identity">
    <p class="identity__company">Desk Ally Worldwide Pty Ltd</p>
    <h1 class="identity__person">Jaakko Virtanola</h1>
    <p class="identity__role">Managing Director</p>
  </div>

  <ul class="contacts">
    <li>
      <svg viewBox="0 0 12 12" aria-hidden="true"><path d="M3 0h6a1 1 0 0 1 1 1v10a1 1 0 0 1-1 1H3a1 1 0 0 1-1-1V1a1 1 0 0 1 1-1zm0 1.5v8h6v-8z"/></svg>
      <span>+61 0432 715 649</span>
    </li>
    <li>
      <svg viewBox="0 0 12 12" aria-hidden="true"><path d="M0 3.5C2 1 10 1 12 3.5L11 5 9 4.3V3.2C7.5 2.6 4.5 2.6 3 3.2v1.1L1 5zM2.5 6h7l1 5h-9z"/></svg>
      <span>+61 02 6187 4326</span>
    </li>
    <li>
      <svg viewBox="0 0 12 12" aria-hidden="true"><path d="M6 0a6 6 0 1 0 3 11.2l-.6-1.1A4.7 4.7 0 1 1 10.7 6v.7c0 .7-.5 1-1 1s-1-.3-1-1V3.5H7.6v.4A2.8 2.8 0 1 0 8 8a2 2 0 0 0 3.9-1.3V6A6 6 0 0 0 6 0zm0 4.4a1.6 1.6 0 1 1 0 3.2 1.6 1.6 0 0 1 0-3.2z"/></svg>
      <span>jaakko@deskallies-example.com.au</span>
    </li>
    <li>
      <svg viewBox="0 0 12 12" aria-hidden="true"><path d="M6 0a4.3 4.3 0 0 0-4.3 4.3C1.7 7.5 6 12 6 12s4.3-4.5 4.3-7.7A4.3 4.3 0 0 0 6 0zm0 6a1.7 1.7 0 1 1 0-3.4A1.7 1.7 0 0 1 6 6z"/></svg>
      <span>3/47 Darrow Lane Belmont ACT 2915</span>
    </li>
    <li>
      <svg viewBox="0 0 12 12" aria-hidden="true"><path d="M6 0a6 6 0 1 0 0 12A6 6 0 0 0 6 0zm4.4 5.3H8.6a9 9 0 0 0-.9-3.8 4.5 4.5 0 0 1 2.7 3.8zM6 1.4c.6.8 1.1 2.2 1.2 3.9H4.8C4.9 3.6 5.4 2.2 6 1.4zM4.3 1.5a9 9 0 0 0-.9 3.8H1.6a4.5 4.5 0 0 1 2.7-3.8zM1.6 6.7h1.8c.1 1.5.4 2.8.9 3.8a4.5 4.5 0 0 1-2.7-3.8zM6 10.6c-.6-.8-1.1-2.2-1.2-3.9h2.4c-.1 1.7-.6 3.1-1.2 3.9zm1.7-.1c.5-1 .8-2.3.9-3.8h1.8a4.5 4.5 0 0 1-2.7 3.8z"/></svg>
      <span>www.deskallies-example.com.au</span>
    </li>
  </ul>
</section>

</body>
</html>
```